Sole Relationship Graphic of Chapter Organization for Book

This design shows relationships between variables associated with footwear and footprints. It will be used as a graphic in a book. The four elements of the graphic are (1) Variables, (2) Book Chapter Numbers (which correspond to the relationship(s) between at least two variables, (3) Relationship Arrows, and (4) Influence Arrows (because the influencers affect the variables differently than relationships between the variables). These names simply relate to the attempts I have made (and attached) at creating a graphic. In the attached diagrams, the circles with numbers are placeholders for the book chapter numbers, which may be changed so it will be good if I can change those after the graphic is completed. Chapter 1 will be the introduction.
The intent of of outsourcing this project is not necessarily sticking to the formats I have attached, but to allow your creativity to produce a useful graphic that can visually make the most sense of the relationships between the variables as chapters to readers of the book.

Target Market(s)

Search and Rescue Trackers

Requirements
Must have
• Information listed in project description, and drafted in attached diagrams
Nice to have
• Can include outlines of barefoot and outsoles. While Chapters 1 (Intro), 2 (Missing Persons' Footwear), 10 (Case Studies) and 11 (Summary) are set, the others aren't. The end game of this book is to use the rest of the variables to arrive at the end game, which is measurements for barefoot track length or outsole track length...so those two variables can be highlighted in some way to emphasize their importance.

```html
<!DOCTYPE html>
<html lang="en">
<head>
<meta charset="utf-8">
<title>Footwear and Track Length: Chapter Relationships</title>
<link rel="stylesheet" href="https://fonts.googleapis.com/css2?family=Dosis:wght@500&display=swap">
<style>
  :root {
    --teal: #40bfb0;
    --blue: #3f57a6;
    --orange: #f5871f;
    --white: #ffffff;
  }
  html, body {
    margin: 0;
    padding: 0;
    overflow: hidden;
    background: var(--white);
  }
  .chart {
    display: block;
    width: 875px;
    height: 1200px;
  }
  .node { fill: var(--teal); }
  .node-label {
    fill: var(--white);
    font-family: "Dosis", sans-serif;
    font-size: 56px;
    font-weight: 500;
    text-anchor: middle;
    text-transform: uppercase;
  }
  .node-label.is-large { font-size: 62px; }
  .node-label.is-small { font-size: 47px; }
  .link {
    fill: none;
    stroke-width: 9;
    stroke-linecap: round;
    stroke-linejoin: round;
  }
  .link.relationship { stroke: var(--blue); }
  .link.influence { stroke: var(--orange); }
  .chapter-badge.relationship { fill: var(--blue); }
  .chapter-badge.influence { fill: var(--orange); }
  .chapter-badge.legend-key { fill: var(--teal); }
  .chapter-number {
    fill: var(--white);
    font-family: "Dosis", sans-serif;
    font-size: 48px;
    font-weight: 500;
    text-anchor: middle;
    dominant-baseline: central;
  }
  .brace { fill: var(--teal); }
  .legend-frame {
    fill: none;
    stroke: var(--teal);
    stroke-width: 9;
  }
  .legend-tab { fill: var(--teal); }
  .legend-title {
    fill: var(--white);
    font-family: "Dosis", sans-serif;
    font-size: 50px;
    font-weight: 500;
    text-anchor: middle;
    text-transform: uppercase;
  }
  .legend-text {
    font-family: "Dosis", sans-serif;
    font-size: 48px;
    font-weight: 500;
    text-transform: uppercase;
  }
  .legend-text.chapter { fill: var(--teal); }
  .legend-text.relationship { fill: var(--blue); }
  .legend-text.influence { fill: var(--orange); }
</style>
</head>
<body>
<svg class="chart" viewBox="0 0 1650 2263" preserveAspectRatio="none" role="img" aria-label="Diagram of how footwear and foot variables relate, labelled by book chapter">

  <!-- Top variable -->
  <g class="variable">
    <ellipse class="node" cx="563" cy="310" rx="205" ry="128"/>
    <text class="node-label is-large" x="556" y="270" textLength="197" lengthAdjust="spacingAndGlyphs">Missing</text>
    <text class="node-label is-large" x="556" y="330" textLength="232" lengthAdjust="spacingAndGlyphs">Persons’</text>
    <text class="node-label is-large" x="562" y="392" textLength="275" lengthAdjust="spacingAndGlyphs">Footwear</text>
  </g>

  <path class="brace" d="M280 618 C300 530 340 500 390 505 C430 508 460 515 500 512 C540 505 555 480 563 455 C571 480 586 505 626 512 C666 515 696 508 736 505 C786 500 826 530 847 618 C826 560 800 545 760 546 C720 547 690 553 655 553 C610 552 580 530 563 470 C546 530 516 552 471 553 C436 553 406 547 366 546 C326 545 300 560 280 618 Z"/>

  <!-- Variables -->
  <g class="variable">
    <ellipse class="node" cx="260" cy="737" rx="145" ry="90"/>
    <text class="node-label" x="260" y="730" textLength="186" lengthAdjust="spacingAndGlyphs">Outsole</text>
    <text class="node-label" x="265" y="781" textLength="157" lengthAdjust="spacingAndGlyphs">Length</text>
  </g>
  <g class="variable">
    <ellipse class="node" cx="922" cy="737" rx="145" ry="90"/>
    <text class="node-label" x="916" y="730" textLength="137" lengthAdjust="spacingAndGlyphs">Insole</text>
    <text class="node-label" x="921" y="781" textLength="157" lengthAdjust="spacingAndGlyphs">Length</text>
  </g>
  <g class="variable">
    <ellipse class="node" cx="1391" cy="737" rx="145" ry="90"/>
    <text class="node-label" x="1391" y="730" textLength="122" lengthAdjust="spacingAndGlyphs">Hook</text>
    <text class="node-label" x="1396" y="781" textLength="97" lengthAdjust="spacingAndGlyphs">Area</text>
  </g>
  <g class="variable">
    <ellipse class="node" cx="505" cy="1025" rx="145" ry="90"/>
    <text class="node-label" x="503" y="1018" textLength="212" lengthAdjust="spacingAndGlyphs">Individual</text>
    <text class="node-label" x="509" y="1069" textLength="205" lengthAdjust="spacingAndGlyphs">Variation</text>
  </g>
  <g class="variable">
    <ellipse class="node" cx="505" cy="1338" rx="145" ry="90"/>
    <text class="node-label" x="504" y="1331" textLength="185" lengthAdjust="spacingAndGlyphs">Nominal</text>
    <text class="node-label" x="510" y="1382" textLength="78" lengthAdjust="spacingAndGlyphs">Size</text>
  </g>
  <g class="variable">
    <ellipse class="node" cx="922" cy="1338" rx="145" ry="90"/>
    <text class="node-label" x="921" y="1357" textLength="212" lengthAdjust="spacingAndGlyphs">Barefoot</text>
  </g>
  <g class="variable">
    <ellipse class="node" cx="1391" cy="1338" rx="145" ry="90"/>
    <text class="node-label" x="1390" y="1357" textLength="140" lengthAdjust="spacingAndGlyphs">Height</text>
  </g>
  <g class="variable outcome">
    <ellipse class="node" cx="260" cy="1683" rx="145" ry="90"/>
    <text class="node-label" x="261" y="1650" textLength="114" lengthAdjust="spacingAndGlyphs">Shod</text>
    <text class="node-label" x="260" y="1701" textLength="131" lengthAdjust="spacingAndGlyphs">Track</text>
    <text class="node-label" x="260" y="1752" textLength="158" lengthAdjust="spacingAndGlyphs">Length</text>
  </g>
  <g class="variable outcome">
    <ellipse class="node" cx="922" cy="1683" rx="145" ry="90"/>
    <text class="node-label is-small" x="922" y="1673" textLength="176" lengthAdjust="spacingAndGlyphs">Barefoot</text>
    <text class="node-label is-small" x="923" y="1724" textLength="246" lengthAdjust="spacingAndGlyphs">Track Length</text>
  </g>

  <!-- Relationship links -->
  <g class="connection">
    <path class="link relationship" d="M435 727 H740 M463 699 L435 727 L463 755 M712 699 L740 727 L712 755"/>
    <circle class="chapter-badge relationship" cx="578" cy="724" r="30"/>
    <text class="chapter-number" x="578" y="724">5</text>
  </g>
  <g class="connection">
    <path class="link relationship" d="M596 1248 L860 842 M816 851 L860 842 L869 886"/>
    <circle class="chapter-badge relationship" cx="702" cy="1082" r="30"/>
    <text class="chapter-number" x="702" y="1082">4</text>
  </g>
  <g class="connection">
    <path class="link relationship" d="M932 862 V1228 M903 891 L932 862 L961 891 M903 1199 L932 1228 L961 1199"/>
    <circle class="chapter-badge relationship" cx="932" cy="1041" r="30"/>
    <text class="chapter-number" x="932" y="1041">9</text>
  </g>
  <g class="connection">
    <path class="link relationship" d="M664 1338 H760 M732 1310 L760 1338 L732 1366"/>
    <circle class="chapter-badge relationship" cx="700" cy="1340" r="30"/>
    <text class="chapter-number" x="700" y="1340">4</text>
  </g>
  <g class="connection">
    <path class="link relationship" d="M1228 1344 L1088 1340 M1116 1312 L1088 1340 L1116 1368"/>
    <circle class="chapter-badge relationship" cx="1165" cy="1340" r="30"/>
    <text class="chapter-number" x="1165" y="1340">8</text>
  </g>
  <g class="connection">
    <path class="link relationship" d="M923 1452 V1568 M895 1540 L923 1568 L951 1540"/>
    <circle class="chapter-badge relationship" cx="923" cy="1503" r="30"/>
    <text class="chapter-number" x="923" y="1503">9</text>
  </g>
  <g class="connection">
    <path class="link relationship" d="M243 873 V1528 M214 1499 L243 1528 L272 1499"/>
    <circle class="chapter-badge relationship" cx="242" cy="1186" r="30"/>
    <text class="chapter-number" x="242" y="1186">6</text>
  </g>

  <!-- Influence links -->
  <g class="connection">
    <path class="link influence" d="M1228 727 H1088 M1116 699 L1088 727 L1116 755"/>
    <circle class="chapter-badge influence" cx="1170" cy="727" r="30"/>
    <text class="chapter-number" x="1170" y="727">3</text>
  </g>
  <g class="connection">
    <path class="link influence" d="M420 932 L330 840 M372 840 L330 840 L330 882"/>
    <circle class="chapter-badge influence" cx="388" cy="896" r="30"/>
    <text class="chapter-number" x="388" y="896">7</text>
  </g>
  <g class="connection">
    <path class="link influence" d="M640 955 L787 808 M745 808 L787 808 L787 850"/>
    <circle class="chapter-badge influence" cx="689" cy="903" r="30"/>
    <text class="chapter-number" x="689" y="903">7</text>
  </g>
  <g class="connection">
    <path class="link influence" d="M502 1132 V1232 M474 1204 L502 1232 L530 1204"/>
    <circle class="chapter-badge influence" cx="501" cy="1168" r="30"/>
    <text class="chapter-number" x="501" y="1168">5</text>
  </g>

  <!-- Legend -->
  <g class="legend">
    <rect class="legend-frame" x="38" y="1917" width="562" height="303" rx="20"/>
    <rect class="legend-tab" x="198" y="1888" width="240" height="58" rx="20"/>
    <text class="legend-title" x="318" y="1934" textLength="157" lengthAdjust="spacingAndGlyphs">Legend</text>

    <circle class="chapter-badge legend-key" cx="113" cy="2003" r="30"/>
    <text class="chapter-number" x="113" y="2003">1</text>
    <text class="legend-text chapter" x="160" y="2020" textLength="215" lengthAdjust="spacingAndGlyphs">Chapter #</text>

    <path class="link relationship" d="M123 2088 H207 M179 2060 L207 2088 L179 2116"/>
    <text class="legend-text relationship" x="226" y="2103" textLength="299" lengthAdjust="spacingAndGlyphs">Relationship to</text>

    <path class="link influence" d="M123 2160 H207 M179 2132 L207 2160 L179 2188"/>
    <text class="legend-text influence" x="226" y="2175" textLength="244" lengthAdjust="spacingAndGlyphs">Influence on</text>
  </g>
</svg>
</body>
</html>
```